One Page Sales Flyer for Wireless Survey- Computer Hardware

I want a designer to create a one page 4 color sales slick to be given to our sales team to sell to the end customers. I would like a visual picture of a heat map so zavvix "heat map wireless" to get an idea of how that image should look.

```html
<!DOCTYPE html>
<html lang="en">
<head>
<meta charset="utf-8">
<title>Kestrel – Wireless Site Survey Flyer</title>
<link rel="stylesheet" href="https://fonts.googleapis.com/css2?family=Oswald:wght@400;500&family=Roboto:wght@300;400&display=swap">
<style>
  :root {
    --brand-blue: #3a9bd8;
    --ink: #2f2f2f;
    --body-ink: #4a4a4a;
    --panel-dark: #1b1b1b;
    --panel-mid: #3a3a3a;
    --paper: #ffffff;
    --backdrop: #e4e4e4;
    --heat-red: #ee7a62;
    --heat-orange: #f6b25a;
    --heat-yellow: #f7dc6a;
    --heat-blue: #9fcbe6;
  }
  * { margin: 0; padding: 0; box-sizing: border-box; }
  html, body { width: 962px; height: 1200px; overflow: hidden; background: var(--backdrop); }
  .flyer {
    position: absolute; left: 31px; top: 20px;
    width: 852px; height: 1098px;
    background: var(--paper);
    transform: scale(1.056); transform-origin: top left;
    font-family: 'Roboto', sans-serif;
    box-shadow: 0 2px 10px rgba(0,0,0,.15);
    overflow: hidden;
  }
  .brand { position: absolute; left: 31px; top: 18px; display: flex; align-items: center; gap: 16px; }
  .brand-square { width: 80px; height: 80px; border-radius: 8px; background: var(--brand-blue); }
  .brand-name { font-family: 'Roboto', sans-serif; font-weight: 400; font-size: 56px; letter-spacing: 2px; color: var(--ink); }
  .headline {
    position: absolute; left: 452px; top: 26px;
    font-family: 'Oswald', sans-serif; font-weight: 500; font-size: 22px; line-height: 28px;
    color: #111; text-transform: uppercase;
  }
  .hero { position: absolute; left: 0; top: 0; width: 852px; height: 470px; }
  .section-title {
    position: absolute; left: 27px;
    font-family: 'Oswald', sans-serif; font-weight: 400; font-size: 21px; color: #222;
    text-transform: uppercase; letter-spacing: -.2px;
  }
  .section-body {
    position: absolute; left: 27px; width: 796px;
    font-weight: 300; font-size: 17.2px; line-height: 21px; color: var(--body-ink);
    text-align: justify;
  }
  .value-tab {
    position: absolute; left: 0; top: 740px; width: 316px; height: 50px;
    background: var(--brand-blue);
    clip-path: polygon(0 0, 300px 0, 316px 50px, 0 50px);
    font-family: 'Oswald', sans-serif; font-size: 21px; color: #fff;
    padding: 12px 0 0 27px; text-transform: uppercase;
  }
  .value-panel {
    position: absolute; left: 0; top: 780px; width: 852px; height: 180px;
    background: radial-gradient(ellipse at 45% 60%, var(--panel-mid), var(--panel-dark) 70%);
  }
  .value-list { position: absolute; list-style: none; width: 370px; }
  .value-list li {
    position: relative; padding-left: 20px; margin-bottom: 12px;
    font-weight: 300; font-size: 16.3px; line-height: 16.5px; color: #f0f0f0;
  }
  .value-list li::before {
    content: ""; position: absolute; left: 0; top: 2px; width: 12px; height: 12px; border-radius: 50%;
    background: var(--brand-blue);
  }
  .value-list li::after {
    content: ""; position: absolute; left: 3px; top: 5.5px; width: 4px; height: 4px;
    border-right: 1.5px solid #fff; border-top: 1.5px solid #fff; transform: rotate(45deg);
  }
  .col-left { left: 48px; top: 805px; }
  .col-right { left: 455px; top: 805px; }
  .footnote { position: absolute; left: 455px; top: 923px; font-weight: 300; font-size: 12px; color: #ddd; }
  .targets { position: absolute; left: 27px; top: 985px; font-weight: 300; font-size: 14.5px; line-height: 19px; color: #222; }
  .contact-bar {
    position: absolute; left: 0; top: 1045px; width: 852px; height: 53px;
    background: var(--brand-blue); color: #fff;
    font-size: 18px; letter-spacing: 1.5px;
  }
  .contact-item { position: absolute; top: 15px; display: flex; align-items: center; gap: 12px; }
  .contact-item svg { width: 19px; height: 19px; }
</style>
</head>
<body>
<main class="flyer">
  <svg class="hero" viewBox="0 0 852 470" aria-hidden="false">
    <defs>
      <linearGradient id="heatTones" x1="0" y1="0" x2="1" y2="0.4">
        <stop offset="0" stop-color="var(--heat-orange)"/>
        <stop offset=".25" stop-color="var(--heat-red)"/>
        <stop offset=".55" stop-color="var(--heat-red)"/>
        <stop offset=".75" stop-color="var(--heat-yellow)"/>
        <stop offset="1" stop-color="var(--heat-blue)"/>
      </linearGradient>
    </defs>
    <polygon role="img" aria-label="Wireless heat map over an office floor plan, showing signal strength in red, orange, yellow and blue zones"
      points="0,145 374,145 406,110 852,110 852,400 655,400 617,442 0,442" fill="url(#heatTones)"/>
    <polyline points="0,136 372,136 404,102 790,102" fill="none" stroke="var(--brand-blue)" stroke-width="6"/>
    <polyline points="852,410 660,410 624,450 128,450" fill="none" stroke="var(--brand-blue)" stroke-width="6"/>
  </svg>

  <div class="brand">
    <div class="brand-square"></div>
    <span class="brand-name">KESTREL</span>
  </div>
  <h1 class="headline">Increase hardware and services<br>spend with wireless site surveys</h1>

  <h2 class="section-title" style="top:484px">What is a wireless site survey or heat map?</h2>
  <p class="section-body" style="top:515px">A wireless site survey is a compilation of reports showing a visual representation of health of your wireless network. This does not only show how strong or weak a wireless signal is in any location it also helps aid in channel and placement to ensure maximum stable data rates are archived even where the single appears strong.</p>

  <h2 class="section-title" style="top:615px">Why do customers need a site survey?</h2>
  <p class="section-body" style="top:650px">Any variety of factors can contribute to an unhealthy wireless network (electrical, motors, materials used in construction, distance, neighboring wireless networks, etc.) and traditional methods that use only blueprints and a computer program to show signal strength have shown to be ineffective.</p>

  <section>
    <div class="value-panel"></div>
    <div class="value-tab">Why should they use you?</div>
    <ul class="value-list col-left">
      <li>42% of businesses report some issues with wireless connectivity and acknowledge its effect on the bottom line*</li>
      <li>Most of these problems are solved through either fine tuning the current equipment (managed services) or purchasing new equipment (incremental sales) of which you can provide both</li>
    </ul>
    <ul class="value-list col-right">
      <li>Being a one-stop shop for all your customer’s IT needs prevents them from needing additional vendors</li>
      <li>The increase of IoT (Internet of things) and BYOD (Bring Your Own Device)</li>
    </ul>
    <p class="footnote">*Ledgerline.com. “Connectivity in the Modern Enterprise”. June 2017</p>
  </section>

  <p class="targets">TARGET CUSTOMERS<br>Distributors, Warehouses, SLED, K-12, Medical / Hospitals, Enterprise F1000, Sports Venues, Stadiums, Hotels, Retail stores</p>

  <footer class="contact-bar">
    <div class="contact-item" style="left:31px">
      <svg viewBox="0 0 20 20"><circle cx="10" cy="10" r="9" fill="none" stroke="#1b1b1b" stroke-width="1.5"/><rect x="5" y="6.5" width="10" height="7" fill="none" stroke="#1b1b1b" stroke-width="1.3"/><polyline points="5,6.5 10,10.5 15,6.5" fill="none" stroke="#1b1b1b" stroke-width="1.3"/></svg>
      <span>info@yourkestrel.com</span>
    </div>
    <div class="contact-item" style="left:356px">
      <svg viewBox="0 0 20 20"><circle cx="10" cy="10" r="9" fill="none" stroke="#1b1b1b" stroke-width="1.5"/><path d="M6.5 5.5 L8.5 5.2 L9.3 7.8 L8.2 8.8 C8.9 10.3 9.8 11.2 11.2 11.8 L12.2 10.7 L14.8 11.5 L14.5 13.5 C10 14 6 10 6.5 5.5 Z" fill="#1b1b1b"/></svg>
      <span>555-014-2290</span>
    </div>
    <div class="contact-item" style="left:574px">
      <svg viewBox="0 0 20 20"><circle cx="10" cy="10" r="9" fill="none" stroke="#1b1b1b" stroke-width="1.5"/><circle cx="10" cy="10" r="5.5" fill="none" stroke="#1b1b1b" stroke-width="1"/><ellipse cx="10" cy="10" rx="2.3" ry="5.5" fill="none" stroke="#1b1b1b" stroke-width="1"/><line x1="4.5" y1="10" x2="15.5" y2="10" stroke="#1b1b1b" stroke-width="1"/></svg>
      <span>www.yourkestrel.com</span>
    </div>
  </footer>
</main>
</body>
</html>
```